Window cleaning and Pressure washing

Truck wrap partial or full/background:
Would like to see a background of a water mark or something related to window cleaning. And or pressure washing.

Doors of the truck:
Need to have my logo printed in big on the doors and with LLC in small after the logo. Need to have my slogan below my logo on the door.
Slogan is; “Affordable 5 star services!”

Sides of the truck:
Want to see window cleaning and Pressure washing on the sides of the truck in big letters with the phone number. Slanted with a shadow effect.
(Would like to see slanted and not slanted) also need to see something that signifies 100% satisfaction or your money back!Preferably a sticker, Or a combination of both. Also need to have residential and commercial somewhere.
Phone number needs to be on here.

Tailgate:
Want to have the services on the back tailgate with the slogan, as well as the 100% money back guarantee sticker.
And the phone number here to!

Back window;
Needs to have the same background as the wrap on the truck or very slimier with the water swiped away Clean with the logo presented as shown in one of the pictures below.

```html
<!DOCTYPE html>
<html lang="en">
<head>
<meta charset="utf-8">
<title>Bright Path LLC – Truck Wrap</title>
<link rel="stylesheet" href="https://fonts.googleapis.com/css2?family=Anton&family=Montserrat:wght@600;700;800&display=swap">
<style>
  :root{
    --blue:#1a7fd6;
    --blue-deep:#0b56b8;
    --blue-light:#2a9de0;
    --orange:#fcab00;
    --white:#ffffff;
    --ink:#1d2b3a;
    --star:#ffd400;
  }
  *{margin:0;padding:0;box-sizing:border-box}
  html,body{width:1200px;height:939px;overflow:hidden;background:var(--white)}
  .canvas{position:relative;width:1200px;height:939px;font-family:"Montserrat",sans-serif;color:var(--white)}
  .art{position:absolute;inset:0}
  .abs{position:absolute;line-height:1;white-space:nowrap}

  /* Door */
  .licensed{left:157px;top:235px;font-size:17px;font-weight:700}
  .insured{left:158px;top:254px;width:142px;height:23px;background:var(--orange);font-size:16px;font-weight:800;letter-spacing:8px;display:flex;align-items:center;justify-content:center;padding-left:6px}
  .brand{left:372px;top:246px;font-size:38px;font-weight:700;line-height:1;letter-spacing:1px}
  .brand-llc{left:515px;top:321px;font-size:13px;font-weight:700}
  .slogan-top{left:375px;top:346px;font-size:22px;font-weight:800}
  .slogan-bottom{left:387px;top:374px;font-size:25px;font-weight:800}

  /* Side */
  .headline{left:633px;top:226px;font-family:"Anton",sans-serif;font-size:33px;line-height:37.5px;color:#eef1f4;text-shadow:2px 2px 0 #2b2f36,3px 3px 2px rgba(0,0,0,.45);transform:skewX(-4deg);white-space:nowrap}
  .side-phone{left:833px;top:214px;font-family:"Anton",sans-serif;font-size:38px;color:#f2f2f2;text-shadow:2px 2px 0 #23262c,-1px -1px 0 #23262c,1px -1px 0 #23262c,-1px 1px 0 #23262c;transform:skewX(-6deg)}
  .sectors{left:856px;top:260px;width:217px;height:22px;background:var(--white);border-radius:2px;color:var(--blue-light);font-size:13px;font-weight:700;display:flex;align-items:center;justify-content:center}

  .guarantee{position:absolute;display:flex;flex-direction:column;align-items:center;line-height:1}
  .guarantee .pct{font-family:"Anton",sans-serif;color:var(--orange);text-shadow:1px 1px 0 #8a5200}
  .guarantee .pill{background:var(--blue-light);border-radius:8px;display:flex;flex-direction:column;align-items:center;color:var(--white);font-family:"Anton",sans-serif}
  .guarantee .back{background:var(--white);color:var(--orange);font-family:"Anton",sans-serif}
  .guarantee .stars{color:var(--star);letter-spacing:3px}
  .guarantee-side{left:1020px;top:293px;width:78px}
  .guarantee-side .pct{font-size:29px}
  .guarantee-side .pill{width:70px;padding:3px 0 2px;font-size:8px;gap:2px;border-bottom:2px solid var(--white)}
  .guarantee-side .back{font-size:5px;padding:1px 6px}
  .guarantee-side .stars{font-size:8px;margin-top:4px}
  .follow{left:1040px;top:372px;font-size:7px;font-weight:600}

  /* Tailgate */
  .services{position:absolute;list-style:none;font-family:"Anton",sans-serif;font-size:27px;color:#f4f5f7;text-shadow:2px 2px 0 #25292f}
  .services li{display:flex;align-items:center;gap:10px;height:41.5px}
  .services svg{flex:none}
  .services-left{left:262px;top:582px}
  .services-right{left:696px;top:582px}
  .tail-phone{left:333px;top:738px;font-size:57px;font-weight:800;letter-spacing:1px}
  .guarantee-tail{left:846px;top:706px;width:108px}
  .guarantee-tail .pct{font-size:41px}
  .guarantee-tail .pill{width:104px;padding:4px 0 3px;background:var(--orange);font-size:12px;gap:2px;border-bottom:3px solid var(--blue-light)}
  .guarantee-tail .back{font-size:8px;padding:1px 6px}
  .guarantee-tail .stars{font-size:12px;margin-top:4px}
</style>
</head>
<body>
<main class="canvas">
  <svg class="art" viewBox="0 0 1200 939" width="1200" height="939" aria-hidden="true">
    <defs>
      <linearGradient id="wrap-blue" x1="0" y1="0" x2="1" y2="1">
        <stop offset="0" stop-color="#2a8ce0"/>
        <stop offset="1" stop-color="#136fcf"/>
      </linearGradient>
      <linearGradient id="afford-fade" x1="0" x2="1">
        <stop offset="0" stop-color="#fcab00" stop-opacity="0"/>
        <stop offset=".3" stop-color="#fcab00"/>
      </linearGradient>
      <linearGradient id="star-band" x1="0" x2="1">
        <stop offset="0" stop-color="#2a9de0"/>
        <stop offset=".75" stop-color="#2a9de0"/>
        <stop offset="1" stop-color="#2a9de0" stop-opacity="0"/>
      </linearGradient>
      <clipPath id="truck-clip">
        <path clip-rule="evenodd" d="M60,258 C62,245 70,240 80,238 L300,208 L357,198 L467,115 L506,102 L637,99 C647,100 651,105 651,108 L665,209 L1132,208 L1140,234 L1099,242 L1099,321 L1137,324 L1136,340 L1099,343 L1093,405 C1092,410 1085,411 1075,412 L1015,412 L1008,308 C990,290 840,290 821,300 L805,403 C803,405 795,406 780,406 L345,412 C338,412 336,410 335,405 L316,319 C300,285 170,285 134,321 L115,322 L115,255 Z M423,228 L598,222 C603,222 606,219 606,214 L606,125 C606,115 598,111 585,111 C540,112 500,118 470,135 L423,170 L395,192 C385,205 390,225 410,229 Z"/>
      </clipPath>
    </defs>

    <!-- Truck side -->
    <g class="truck-side" clip-path="url(#truck-clip)">
      <rect x="50" y="90" width="1100" height="330" fill="url(#wrap-blue)" role="img" aria-label="Blue water-droplet background"/>
      <polygon points="560,250 650,222 700,300 740,412 680,412 612,330" fill="var(--blue-deep)"/>
      <rect x="324" y="341" width="236" height="29" rx="3" fill="url(#afford-fade)"/>
      <rect x="368" y="367" width="370" height="37" rx="2" fill="url(#star-band)"/>
      <path d="M786,208 L1150,204 L1150,238 L1100,244 L845,261 C818,262 806,252 800,240 Z" fill="var(--orange)"/>
      <rect x="547" y="254" width="62" height="10" rx="5" fill="var(--white)"/>
    </g>
    <!-- Side phone icon -->
    <circle cx="800" cy="235" r="18" fill="var(--blue-light)" stroke="var(--white)" stroke-width="2.5"/>
    <path d="M793,227 c2,-2 4,-1 5,1 l2,4 c0,2 -2,2 -2,3 c1,3 3,5 6,6 c1,0 1,-2 3,-2 l4,2 c2,1 3,3 1,5 c-3,3 -9,2 -15,-4 c-6,-6 -7,-12 -4,-15z" fill="var(--white)"/>
    <!-- Social placeholders -->
    <circle cx="1048" cy="391" r="6.5" fill="var(--white)"/>
    <circle cx="1067" cy="391" r="6.5" fill="var(--white)"/>

    <!-- Tailgate -->
    <g class="tailgate">
      <path d="M233,533 L248,533 L252,566 L950,566 L954,536 L968,536 L970,816 L232,816 Z" fill="url(#wrap-blue)" role="img" aria-label="Blue water-droplet background"/>
      <path d="M229,728 L970,728 L970,816 L229,816 Z" fill="var(--white)"/>
      <path d="M229,728 L270,728 L324,816 L232,816 Z" fill="var(--blue-light)"/>
      <path d="M264,728 L800,728 C815,728 820,735 825,742 L860,816 L322,816 C310,800 290,760 264,728 Z" fill="var(--orange)"/>
      <path d="M536,586 C536,579 541,577 548,577 L658,577 C665,577 668,580 667,587 L662,625 C660,633 655,637 646,637 L558,637 C549,637 543,633 541,625 Z" fill="var(--white)"/>
      <path d="M536,666 C536,659 541,658 548,658 L658,658 C665,658 668,661 667,668 L662,706 C660,714 655,718 646,718 L558,718 C549,718 543,714 541,706 Z" fill="var(--white)"/>
      <circle cx="287" cy="774" r="28" fill="var(--orange)" stroke="var(--white)" stroke-width="3"/>
      <path d="M276,760 c3,-3 6,-2 8,1 l3,6 c1,3 -2,3 -3,5 c1,5 5,9 10,10 c2,0 2,-3 5,-3 l6,3 c3,2 4,5 1,8 c-5,5 -14,3 -23,-6 c-9,-9 -12,-19 -7,-24z" fill="var(--white)"/>
    </g>
  </svg>

  <!-- Door -->
  <div class="abs licensed">LICENSED AND</div>
  <div class="abs insured">INSURED</div>
  <div class="abs brand">BRIGHT<br>PATH</div>
  <div class="abs brand-llc">LLC</div>
  <div class="abs slogan-top">AFFORDABLE</div>
  <div class="abs slogan-bottom">5 STAR SERVICES!</div>

  <!-- Side -->
  <h1 class="abs headline">WINDOW<br>CLEANING AND<br>PRESSURE<br>WASHING</h1>
  <div class="abs side-phone">(555) 014-2290</div>
  <div class="abs sectors">Commercial &amp; Residential</div>
  <div class="guarantee guarantee-side">
    <span class="pct">100%</span>
    <span class="pill">SATISFACTION OR<span class="back">YOUR MONEY BACK!</span></span>
    <span class="stars">★★★★★</span>
  </div>
  <div class="abs follow">Follow Us</div>

  <!-- Tailgate -->
  <ul class="services services-left">
    <li><svg width="24" height="24" viewBox="0 0 24 24"><circle cx="12" cy="12" r="10" fill="#fff" stroke="#fcab00" stroke-width="2.5"/><path d="M7,12 l3.5,3.5 l6.5,-7" fill="none" stroke="#fcab00" stroke-width="2.5"/></svg>WINDOW CLEANING</li>
    <li><svg width="24" height="24" viewBox="0 0 24 24"><circle cx="12" cy="12" r="10" fill="#fff" stroke="#fcab00" stroke-width="2.5"/><path d="M7,12 l3.5,3.5 l6.5,-7" fill="none" stroke="#fcab00" stroke-width="2.5"/></svg>HOUSE WASHING</li>
    <li><svg width="24" height="24" viewBox="0 0 24 24"><circle cx="12" cy="12" r="10" fill="#fff" stroke="#fcab00" stroke-width="2.5"/><path d="M7,12 l3.5,3.5 l6.5,-7" fill="none" stroke="#fcab00" stroke-width="2.5"/></svg>PRESSURE WASHING</li>
  </ul>
  <ul class="services services-right">
    <li><svg width="24" height="24" viewBox="0 0 24 24"><circle cx="12" cy="12" r="10" fill="#fff" stroke="#fcab00" stroke-width="2.5"/><path d="M7,12 l3.5,3.5 l6.5,-7" fill="none" stroke="#fcab00" stroke-width="2.5"/></svg>ROOF CLEANING</li>
    <li><svg width="24" height="24" viewBox="0 0 24 24"><circle cx="12" cy="12" r="10" fill="#fff" stroke="#fcab00" stroke-width="2.5"/><path d="M7,12 l3.5,3.5 l6.5,-7" fill="none" stroke="#fcab00" stroke-width="2.5"/></svg>GUTTER CLEANING</li>
    <li><svg width="24" height="24" viewBox="0 0 24 24"><circle cx="12" cy="12" r="10" fill="#fff" stroke="#fcab00" stroke-width="2.5"/><path d="M7,12 l3.5,3.5 l6.5,-7" fill="none" stroke="#fcab00" stroke-width="2.5"/></svg>SCREEN REPAIRS</li>
  </ul>
  <div class="abs tail-phone">(555) 014-2290</div>
  <div class="guarantee guarantee-tail">
    <span class="pct">100%</span>
    <span class="pill">SATISFACTION OR<span class="back">YOUR MONEY BACK!</span></span>
    <span class="stars">★★★★★</span>
  </div>
</main>
</body>
</html>
```